Community Management Cooperative Needs a Postcard Design

This will be the first postcard in a 3 part series to be sent to 2,500 management companies in the United States. Neighborhood & Residents Purchasing Alliance helps management companies and communities save money by combining their buying power to drive down costs on everyday business needs. Their membership in the cooperative also connects with other like minded companies in the industry allowing them to share ideas and best practices with one another so that they may improve their business practices. Visit http://joinvelarta.com for more information about the company.

The purpose of this postcard is to get potential members to visit our website to find out more about the cooperative and hopefully apply to become a member. This postcard should convey a message along the lines of "we want you" or "joining forces". I would like to use bright colors and make it eye catching. Can be things along the lines of (but not limited to) super heroes coming together or a patriotic theme, etc. Postcard does not have to be limited to company color palette but provided for reference.
Updates

Target Market(s)

Independent community management companies in the United States, mostly around metropolitan areas. CEO's of companies are usually male and older, 50+

Industry/Entity Type

Community

Requirements
Must have
• Must incorporate our name, logo, and website into the design with a call to action to visit the website.
• http://joinvelarta.com

```html
<!DOCTYPE html>
<html lang="en">
<head>
<meta charset="utf-8">
<title>Neighborhood &amp; Residents Purchasing Alliance Postcard</title>
<link rel="stylesheet" href="https://fonts.googleapis.com/css2?family=Source+Sans+3:wght@300;400;600;700&display=swap">
<style>
  :root {
    --plum: #6d2254;
    --plum-dark: #5a1a45;
    --lime: #b7d02f;
    --white: #ffffff;
    --panel-light: rgba(255,255,255,0.55);
    --panel-mid: rgba(235,235,235,0.75);
    --line-grey: #c9c9c9;
    --photo-light: #f1f0ef;
    --photo-dark: #3a2a35;
  }
  * { box-sizing: border-box; margin: 0; padding: 0; }
  html, body { width: 1200px; height: 777px; overflow: hidden; background: var(--white); }
  body { font-family: "Source Sans 3", "Helvetica Neue", Arial, sans-serif; position: relative; }

  .postcard-front { position: absolute; left: 0; top: 0; width: 795px; height: 670px; overflow: hidden; }

  .hero-photo {
    position: absolute; left: 0; top: 0; width: 795px; height: 548px;
    background:
      radial-gradient(ellipse 55% 60% at 50% 45%, #7a5a6c 0%, #4a3541 45%, transparent 75%),
      linear-gradient(90deg, var(--photo-light) 0%, #d9d6d7 22%, #5b4a54 45%, #3a2a35 60%, #d8d5d6 82%, var(--photo-light) 100%);
  }

  .headline {
    position: absolute; left: 0; top: 30px; width: 530px; height: 76px;
    background: var(--plum); color: var(--white);
    font-weight: 300; font-size: 29px; line-height: 31px;
    padding: 6px 0 0 32px;
  }
  .headline span { display: block; }
  .headline span + span { padding-left: 26px; }

  .rule-lime { position: absolute; left: 0; width: 795px; height: 9px; background: var(--lime); }
  .rule-top { top: 342px; }
  .rule-bottom { top: 540px; }

  .benefits { position: absolute; left: 0; top: 351px; width: 795px; height: 167px; display: flex; }
  .benefit { position: relative; flex: 0 0 auto; height: 100%; }
  .benefit:nth-child(1) { width: 270px; background: var(--panel-light); }
  .benefit:nth-child(2) { width: 250px; background: var(--panel-mid); }
  .benefit:nth-child(3) { width: 275px; background: var(--panel-light); }
  .benefit-icon { position: absolute; left: 50%; top: 3px; width: 112px; height: 112px; margin-left: -56px; }
  .benefit-label {
    position: absolute; left: 0; right: 0; bottom: 0; height: 46px;
    background: var(--plum); color: var(--white);
    font-size: 15.5px; line-height: 19px; text-align: center; padding-top: 4px;
  }
  .benefit:nth-child(2) .benefit-label { background: #8a4a74; }
  .benefit-label strong { font-weight: 700; }

  .footer-band {
    position: absolute; left: 0; top: 549px; width: 795px; height: 121px;
    background: var(--plum);
  }
  .site-url { position: absolute; left: 32px; top: 48px; color: var(--white); font-size: 27px; font-weight: 300; }
  .site-url b { color: var(--lime); font-weight: 600; }
  .brand { position: absolute; left: 486px; top: 20px; display: flex; align-items: center; gap: 14px; }
  .brand-mark { width: 74px; height: 74px; border: 2px solid var(--white); }
  .brand-name {
    color: var(--white); font-weight: 600; font-size: 17px; line-height: 21px;
    letter-spacing: 2.5px; text-transform: uppercase; width: 230px;
  }

  .postcard-back .stamp-box {
    position: absolute; left: 1008px; top: 21px; width: 168px; height: 171px;
    border: 1.5px solid var(--line-grey);
  }
  .address-line { position: absolute; left: 843px; width: 318px; height: 0; border-top: 1.5px solid var(--line-grey); }
</style>
</head>
<body>
  <section class="postcard-front">
    <div class="hero-photo" role="img" aria-label="Photo of a business team stacking their hands together in a joined huddle"></div>

    <h1 class="headline"><span>Making Independent</span><span>Management Companies Stronger</span></h1>

    <div class="rule-lime rule-top"></div>

    <div class="benefits">
      <div class="benefit">
        <svg class="benefit-icon" viewBox="0 0 112 112" aria-hidden="true">
          <circle cx="56" cy="56" r="54" fill="#6d2254"/>
          <circle cx="56" cy="56" r="43" fill="none" stroke="#fff" stroke-width="3"/>
          <text x="52" y="74" text-anchor="middle" font-family="Source Sans 3, sans-serif" font-weight="700" font-size="52" fill="#fff">$</text>
          <circle cx="67" cy="70" r="9" fill="#fff"/>
          <rect x="65.5" y="63" width="3" height="9" fill="#6d2254"/>
          <rect x="65.5" y="74" width="3" height="3" fill="#6d2254"/>
        </svg>
        <p class="benefit-label"><strong>Save money</strong> by combining your<br>buying power to drive down costs</p>
      </div>
      <div class="benefit">
        <svg class="benefit-icon" viewBox="0 0 112 112" aria-hidden="true">
          <circle cx="56" cy="56" r="54" fill="#6d2254"/>
          <circle cx="56" cy="56" r="43" fill="none" stroke="#fff" stroke-width="3"/>
          <g stroke="#fff" stroke-width="3">
            <line x1="50" y1="58" x2="70" y2="38"/>
            <line x1="50" y1="58" x2="70" y2="74"/>
            <line x1="50" y1="58" x2="36" y2="58"/>
          </g>
          <g fill="#fff">
            <circle cx="50" cy="58" r="8"/>
            <circle cx="70" cy="38" r="6"/>
            <circle cx="70" cy="74" r="6"/>
            <circle cx="36" cy="58" r="5"/>
          </g>
        </svg>
        <p class="benefit-label"><strong>Share ideas</strong> and connect with<br>other like minded companies</p>
      </div>
      <div class="benefit">
        <svg class="benefit-icon" viewBox="0 0 112 112" aria-hidden="true">
          <circle cx="56" cy="56" r="54" fill="#6d2254"/>
          <circle cx="56" cy="56" r="43" fill="none" stroke="#fff" stroke-width="3"/>
          <rect x="32" y="36" width="48" height="36" fill="none" stroke="#fff" stroke-width="2.5"/>
          <g fill="#fff">
            <rect x="37" y="58" width="5" height="11"/>
            <rect x="45" y="52" width="5" height="17"/>
            <rect x="53" y="55" width="5" height="14"/>
            <rect x="61" y="46" width="5" height="23"/>
            <rect x="69" y="41" width="5" height="28"/>
          </g>
        </svg>
        <p class="benefit-label"><strong>Improve</strong> your<br>business practices</p>
      </div>
    </div>

    <div class="rule-lime rule-bottom"></div>

    <footer class="footer-band">
      <p class="site-url">www.join<b>velarta</b>.com</p>
      <div class="brand">
        <span class="brand-mark" aria-hidden="true"></span>
        <span class="brand-name">Neighborhood &amp; Residents Purchasing Alliance</span>
      </div>
    </footer>
  </section>

  <section class="postcard-back" aria-label="Mailing side">
    <div class="stamp-box"></div>
    <div class="address-line" style="top:447px"></div>
    <div class="address-line" style="top:501px"></div>
    <div class="address-line" style="top:555px"></div>
    <div class="address-line" style="top:609px"></div>
  </section>
</body>
</html>
```